GILDED BRICKWORK: THE DEPENDABLE ROUTE WHEREBY MODEST HOUSING FLIPS YIELD HANDSOME RETURNS

I am looking for a book cover design for my new E-Book.

My idea for the design is a pin board with before and after photos of our properties pinned on it (example attached). I have also attached some photos to use.

PLEASE SUBMIT OTHER DESIGNS ALSO AS THIS WAS JUST AN IDEA BUT I AM OPEN TO OTHER IDEAS ALSO.

Page size is 5x7 inches

Font styles to use
Serif
Sans Serif

Colors
0255a3
3176b5
85acd3
85cae6
33a6d7
0392cd
9bcb3c
abd036
ec1f27

```html
<!DOCTYPE html>
<html lang="en">
<head>
<meta charset="utf-8">
<title>Gilded Brickwork – E-Book Cover</title>
<link href="https://fonts.googleapis.com/css2?family=Oswald:wght@400;500;600;700&display=swap" rel="stylesheet">
<style>
  :root {
    --page-bg: #ffffff;
    --title-blue: #17488b;
    --title-text: #ffffff;
    --band-green: #7cc242;
    --band-red: #d62a2b;
    --subtitle-ink: #1a1a1a;
    --photo-warm: #b98a6c;
    --photo-neutral: #c9c6c1;
    --photo-light: #e2e0dc;
  }
  * { margin: 0; padding: 0; box-sizing: border-box; }
  html, body {
    width: 1200px;
    height: 1186px;
    overflow: hidden;
    background: var(--page-bg);
  }
  .canvas {
    position: relative;
    width: 1200px;
    height: 1186px;
    background: var(--page-bg);
  }
  .cover {
    position: absolute;
    left: 187px;
    top: 43px;
    width: 826px;
    height: 1100px;
    display: flex;
    flex-direction: column;
    font-family: 'Oswald', sans-serif;
    overflow: hidden;
  }
  .title-block {
    height: 406px;
    background: var(--title-blue);
    color: var(--title-text);
    display: flex;
    flex-direction: column;
    align-items: center;
    justify-content: center;
    text-transform: uppercase;
    line-height: 1;
    padding: 14px 40px 0;
    white-space: nowrap;
  }
  .title-line--top {
    font-size: 124px;
    font-weight: 500;
    letter-spacing: 2px;
  }
  .title-line--main {
    font-size: 138px;
    font-weight: 700;
    letter-spacing: 1px;
    margin-top: 4px;
  }
  .hero-photo {
    height: 406px;
    background: linear-gradient(100deg, var(--photo-warm) 0%, var(--photo-neutral) 45%, var(--photo-light) 100%);
  }
  .subtitle-band {
    height: 138px;
    background: var(--band-green);
    color: var(--subtitle-ink);
    display: flex;
    flex-direction: column;
    align-items: center;
    justify-content: center;
    text-transform: uppercase;
    font-size: 37px;
    font-weight: 400;
    line-height: 1.15;
    text-align: center;
    white-space: nowrap;
  }
  .author-band {
    height: 150px;
    background: var(--band-red);
    color: var(--title-text);
    display: flex;
    align-items: center;
    justify-content: center;
    font-size: 72px;
    font-weight: 500;
    padding-bottom: 6px;
  }
</style>
</head>
<body>
  <div class="canvas">
    <div class="cover">
      <header class="title-block">
        <span class="title-line--top">Gilded</span>
        <span class="title-line--main">Brickwork</span>
      </header>
      <div class="hero-photo" role="img" aria-label="Photo of a room mid-renovation changing into a finished interior, with banknotes floating through the air"></div>
      <div class="subtitle-band">
        <span>The dependable route whereby modest</span>
        <span>housing flips yield handsome returns</span>
      </div>
      <footer class="author-band">Marcus Whitford</footer>
    </div>
  </div>
</body>
</html>
```